Thornwick Estates Managment Ltd website

Need a website To inform people/clients of the services we provide. 5 pages total with a local feel. Bristol, UK. I have logo artwork already is like the look based on
incorporate the artwork attached for theme, feel and colours fonts info etc

To best describe the business have a brief look at www.fernbaylettings.co.uk which is a local firm offering the same services. This is for your ref only and not to be copied.

Target Market(s)

Property Investors/Landlords

Coding

Coded - Design and coding required

Number of Pages Required

5+ page

Colors
0392cd
f68d4d

Requirements
Must have
• local feel. Possibly using some local architecture or historic landmarks etc. This is fexible.
• most also be mobile device compatible
Nice to have
• the membership logos - files attached: KTB, GHW, DVT and safebondhold.co.uk

```html
<!DOCTYPE html>
<html lang="en">
<head>
<meta charset="utf-8">
<title>Thornwick Estates Managment Ltd</title>
<link rel="stylesheet" href="https://fonts.googleapis.com/css2?family=Montserrat:wght@400;500;600;700&display=swap">
<style>
  :root {
    --orange: #f68d4d;
    --blue: #0392cd;
    --white: #ffffff;
    --text: #3c3c3c;
    --muted: #a8a8a8;
    --panel: #dcdde0;
    --footer: #262626;
    --footer-line: #3a3a3a;
    --field-border: #4a4a4a;
  }
  * { box-sizing: border-box; margin: 0; padding: 0; }
  html, body { width: 1200px; height: 2659px; overflow: hidden; }
  body { font-family: "Montserrat", sans-serif; color: var(--text); background: var(--white); position: relative; }

  /* Hero */
  .hero { position: absolute; left: 0; top: 0; width: 1200px; height: 674px; }
  .hero-photo { position: absolute; inset: 0;
    background: linear-gradient(180deg, #2b3a52 0%, #4d5a6e 35%, #b98a55 58%, #5a4330 72%, #1e1a17 100%); }
  .hero-photo::after { content: ""; position: absolute; inset: 0;
    background: radial-gradient(ellipse at 88% 55%, rgba(255,200,120,.55), transparent 45%); }
  .brand { position: absolute; left: 99px; top: 46px; display: flex; align-items: center; gap: 10px;
    color: var(--white); font-weight: 700; font-size: 22px; }
  .brand-mark { width: 30px; height: 30px; background: var(--white); }
  .nav { position: absolute; top: 58px; display: flex; font-size: 12px; font-weight: 600; color: var(--white); }
  .nav a { position: absolute; white-space: nowrap; color: inherit; text-decoration: none; }
  .btn-contact { position: absolute; left: 932px; top: 44px; width: 169px; height: 41px; background: var(--orange);
    color: var(--white); font-size: 14px; font-weight: 600; display: flex; align-items: center; justify-content: center; }
  .hero-title { position: absolute; left: 0; width: 1200px; top: 306px; text-align: center; color: var(--white);
    font-size: 31px; font-weight: 700; letter-spacing: .5px; }
  .hero-sub { position: absolute; left: 380px; width: 440px; top: 350px; text-align: center; color: var(--white);
    font-size: 14px; font-weight: 500; line-height: 21px; letter-spacing: 1px; }

  /* Services */
  .services { position: absolute; left: 0; top: 674px; width: 1200px; height: 393px; }
  .service { position: absolute; top: 66px; width: 240px; text-align: center; }
  .service svg { display: block; margin: 0 auto; }
  .service-title { margin-top: 28px; font-size: 12px; letter-spacing: 1.5px; color: #555; }
  .service-text { margin-top: 22px; font-size: 12px; line-height: 19px; color: var(--muted); padding: 0 10px; }
  .service-link { margin-top: 20px; font-size: 10px; letter-spacing: 1.5px; color: #555; }

  /* Features */
  .features { position: absolute; left: 0; top: 1067px; width: 1200px; height: 842px; background: var(--panel); }
  .feature-photo, .feature-copy { position: absolute; width: 441px; height: 324px; }
  .feature-copy { background: var(--white); padding: 46px 42px 0; }
  .feature-copy h2 { font-size: 17px; font-weight: 500; line-height: 22px; letter-spacing: 1px; color: #444; }
  .feature-copy p { margin-top: 10px; font-size: 11px; line-height: 19.5px; color: var(--muted); }
  .btn-outline { position: absolute; width: 169px; height: 41px; border: 1px solid var(--orange); color: var(--orange);
    font-size: 12px; letter-spacing: 1.5px; display: flex; align-items: center; justify-content: center; }

  /* Memberships */
  .memberships { position: absolute; left: 0; top: 1909px; width: 1200px; height: 138px; background: var(--white); }
  .badge { position: absolute; }

  /* Footer */
  .footer { position: absolute; left: 0; top: 2047px; width: 1200px; height: 612px; background: var(--footer); color: var(--white); }
  .footer h3 { position: absolute; font-size: 21px; font-weight: 600; }
  .about-text { position: absolute; left: 101px; top: 126px; width: 426px; font-size: 14px; line-height: 25px; text-align: justify; }
  .contact-lines { position: absolute; left: 99px; top: 348px; font-size: 14px; line-height: 25px; }
  .field { position: absolute; left: 675px; width: 426px; border: 1px solid var(--field-border);
    font-size: 14px; color: #6d6d6d; padding: 10px 14px; }
  .btn-send { position: absolute; left: 677px; top: 420px; width: 169px; height: 41px; background: var(--orange);
    font-size: 14px; font-weight: 600; display: flex; align-items: center; justify-content: center; }
  .footer-rule { position: absolute; left: 0; top: 516px; width: 1200px; height: 1px; background: var(--footer-line); }
  .copyright { position: absolute; left: 99px; top: 557px; font-size: 13px; color: #7a7a7a; }
  .social { position: absolute; left: 930px; top: 556px; display: flex; gap: 20px; align-items: center; }
  .social span { width: 16px; height: 16px; border-radius: 50%; background: #8a8a8a; display: block; }
</style>
</head>
<body>

<header class="hero">
  <div class="hero-photo" role="img" aria-label="Bristol skyline at sunset with a classical columned monument silhouetted on the left"></div>
  <div class="brand"><span class="brand-mark"></span>Thornwick</div>
  <nav class="nav">
    <a style="left:523px">Home</a>
    <a style="left:610px">Landlords</a>
    <a style="left:680px">Agencies</a>
    <a style="left:764px">About Us</a>
    <a style="left:851px">Contact</a>
  </nav>
  <div class="btn-contact">CONTACT US</div>
  <h1 class="hero-title">THORNWICK ESTATES MANAGEMENT</h1>
  <p class="hero-sub">THE PERFECT SOLUTION FOR LANDLORDS, TENANTS &amp; AGENCIES IN BRISTOL</p>
</header>

<section class="services">
  <div class="service" style="left:192px">
    <svg width="56" height="68" viewBox="0 0 56 68" fill="none" stroke="#333" stroke-width="2">
      <circle cx="28" cy="22" r="13"/><path d="M15 20 q13 -16 26 0"/><path d="M6 66 v-14 q0 -12 22 -14 q22 2 22 14 v14"/><path d="M22 40 l6 10 l6 -10"/>
    </svg>
    <div class="service-title">FOR LANDLORDS</div>
    <p class="service-text">Lorem ipsum dolor sit amet, consectetur adipisicing elit, sed do eiusmod tempor incididunt ut labore et dolore magna aliqua.</p>
    <div class="service-link">DISCOVER</div>
  </div>
  <div class="service" style="left:476px">
    <svg width="56" height="68" viewBox="0 0 56 68" fill="none" stroke="#333" stroke-width="2">
      <circle cx="28" cy="22" r="13"/><path d="M14 16 q14 -14 28 0"/><path d="M6 66 v-14 q0 -12 22 -14 q22 2 22 14 v14"/><path d="M28 40 v18"/>
    </svg>
    <div class="service-title">FOR TENANTS</div>
    <p class="service-text">Lorem ipsum dolor sit amet, consectetur adipisicing elit, sed do eiusmod tempor incididunt ut labore et dolore magna aliqua.</p>
    <div class="service-link">CONTACT US</div>
  </div>
  <div class="service" style="left:761px">
    <svg width="70" height="68" viewBox="0 0 70 68" fill="none" stroke="#333" stroke-width="2">
      <circle cx="18" cy="22" r="9"/><circle cx="52" cy="22" r="9"/><circle cx="35" cy="26" r="12"/>
      <path d="M2 56 v-8 q0 -10 14 -12"/><path d="M68 56 v-8 q0 -10 -14 -12"/><path d="M14 66 v-10 q0 -14 21 -15 q21 1 21 15 v10"/>
    </svg>
    <div class="service-title">FOR AGENCIES</div>
    <p class="service-text">Lorem ipsum dolor sit amet, consectetur adipisicing elit, sed do eiusmod tempor incididunt ut labore et dolore magna aliqua.</p>
    <div class="service-link">DISCOVER</div>
  </div>
</section>

<section class="features">
  <div class="feature-photo" style="left:154px;top:96px;background:linear-gradient(160deg,#8fa3b8 0%,#c9cfd6 40%,#6b7a86 70%,#8a3a3a 100%)" role="img" aria-label="Two people carrying a red canoe in front of a mirrored sphere building"></div>
  <div class="feature-copy" style="left:595px;top:96px">
    <h2>WE PROVIDE QUALITY<br>ACCOMMODATION</h2>
    <p>Lorem ipsum dolor sit amet, consectetur adipisicing elit, sed do eiusmod tempor incididunt ut labore et dolore magna aliqua. Ut enim ad minim veniam, quis nostrud exercitation ullamco laboris nisi ut aliquip ex ea commodo consequat. Duis aute irure dolor in reprehenderit in voluptate velit esse cillum dolore eu fugiat nulla pariatur.</p>
    <div class="btn-outline" style="left:240px;top:251px">READ MORE</div>
  </div>
  <div class="feature-copy" style="left:154px;top:420px">
    <h2>WE ACQUIRE OUR PROPERTY ASSETS<br>IN 3 DIFFERENT WAYS</h2>
    <p>Lorem ipsum dolor sit amet, consectetur adipisicing elit, sed do eiusmod tempor incididunt ut labore et dolore magna aliqua. Ut enim ad minim veniam, quis nostrud exercitation ullamco laboris nisi ut aliquip ex ea commodo consequat. Duis aute irure dolor in reprehenderit in voluptate velit esse cillum dolore eu fugiat nulla pariatur.</p>
    <div class="btn-outline" style="left:238px;top:251px">READ MORE</div>
  </div>
  <div class="feature-photo" style="left:595px;top:420px;background:linear-gradient(180deg,#3d5f8c 0%,#7f9bbd 35%,#c07a45 65%,#2e2a2a 100%)" role="img" aria-label="Illuminated city square at dusk with a glass sphere and a steel water sculpture"></div>
</section>

<section class="memberships">
  <div class="badge" style="left:175px;top:38px;width:64px;height:64px;background:#2a9aa8" role="img" aria-label="KTB membership badge"></div>
  <div class="badge" style="left:340px;top:56px;width:258px;height:28px;background:#2a9aa8;border-radius:3px" role="img" aria-label="safebondhold.co.uk membership badge"></div>
  <div class="badge" style="left:686px;top:40px;width:82px;height:60px;background:#8c1c24" role="img" aria-label="GHW membership badge"></div>
  <div class="badge" style="left:864px;top:47px;width:186px;height:44px;background:#9b4fa3;border-radius:3px" role="img" aria-label="DVT membership badge"></div>
</section>

<footer class="footer">
  <h3 style="left:101px;top:76px">ABOUT US</h3>
  <p class="about-text">Lorem ipsum dolor sit amet, consectetur adipisicing elit, sed do eiusmod tempor incididunt ut labore et dolore magna aliqua. Ut enim ad minim veniam, quis nostrud exercitation ullamco laboris nisi ut aliquip ex ea commodo consequat. Duis aute irure dolor in reprehenderit in voluptate velit esse cillum dolore eu fugiat nulla pariatur.</p>
  <h3 style="left:101px;top:304px">CONTACT</h3>
  <div class="contact-lines">
    Email: hello@thornwickestates.co.uk<br>
    Telephone: 0117 496 0731
  </div>

  <h3 style="left:674px;top:76px">CONTACT US</h3>
  <div class="field" style="top:130px;height:41px">Email</div>
  <div class="field" style="top:188px;height:43px">Phone Number</div>
  <div class="field" style="top:247px;height:150px">Message</div>
  <div class="btn-send">SEND MESSAGE</div>

  <div class="footer-rule"></div>
  <div class="copyright">© 2016 Thornwick Estates Managment Ltd.</div>
  <div class="social">
    <span></span><span></span><span></span><span></span>
    <svg width="18" height="14" viewBox="0 0 18 14" fill="none" stroke="#8a8a8a" stroke-width="1.6"><rect x="1" y="1" width="16" height="12"/><path d="M1 1 l8 7 l8 -7"/></svg>
  </div>
</footer>

</body>
</html>
```